Small Business Consulting Firm Needs Business Card Design

Need a sleek modern business card with 2 sides matching the colors of our logo. We will be placing these with a mailer we are sending out. These business cards will only ever be given to business owners. We operate helping businesses who are struggling with cash flow or finances. If the green and blue design needs to be moved to the right of "Harborline Crest Consulting" for aesthetic purposes that is ok. We will need an editable file if possible. We would like to include the reps name, email, website, and phone number. For now just use Peter Vance, pvance@harborlinecrest.com, www.harborlinecrest.com, and 833-555-0172.

```html
<!DOCTYPE html>
<html lang="en">
<head>
<meta charset="utf-8">
<title>Harborline Crest Consulting – Business Card</title>
<link rel="stylesheet" href="https://fonts.googleapis.com/css2?family=Lato:wght@400&family=Open+Sans:wght@300;400;700&display=swap">
<style>
  :root {
    --navy: #061636;
    --green: #7bc043;
    --white: #ffffff;
    --ink: #0b0b0b;
  }
  * { margin: 0; padding: 0; box-sizing: border-box; }
  html, body {
    width: 1200px;
    height: 688px;
    overflow: hidden;
    background: var(--white);
  }
  .card {
    position: relative;
    width: 1200px;
    height: 688px;
    background: var(--white);
    overflow: hidden;
  }
  .brand-panel {
    position: absolute;
    left: 0; top: 0;
    width: 545px; height: 688px;
    background: var(--navy);
  }
  .divider-line {
    position: absolute;
    left: 545px; top: 0;
    width: 9px; height: 688px;
    background: var(--green);
  }
  .brand {
    position: absolute;
    left: 0; width: 545px;
    top: 318px;
    text-align: center;
    color: var(--white);
    font-family: "Open Sans", sans-serif;
    font-weight: 400;
  }
  .brand-mark {
    display: block;
    width: 34px; height: 34px;
    margin: 0 auto 26px;
    background: var(--green);
  }
  .brand-name {
    display: block;
    font-size: 26px;
    letter-spacing: 1.5px;
    line-height: 1;
    text-transform: uppercase;
  }
  .brand-tagline {
    display: block;
    margin-top: 12px;
    font-size: 14px;
    letter-spacing: 6px;
    line-height: 1;
    text-transform: uppercase;
  }
  .contact-rail {
    position: absolute;
    left: 514px; top: 146px;
    width: 72px; height: 407px;
  }
  .side-tab {
    position: absolute;
    left: 1167px; top: 177px;
    width: 40px; height: 336px;
    border-radius: 34px 0 0 34px;
    background: var(--green);
  }
  .rep-name {
    position: absolute;
    left: 611px; top: 152px;
    font-family: "Open Sans", sans-serif;
    font-size: 62px;
    line-height: 1;
    color: var(--ink);
    letter-spacing: 0.5px;
    white-space: nowrap;
  }
  .rep-name .first { font-weight: 700; }
  .rep-name .last { font-weight: 300; }
  .contact-item {
    position: absolute;
    left: 612px;
    font-family: "Lato", sans-serif;
    font-size: 27px;
    line-height: 1;
    color: var(--ink);
    white-space: nowrap;
  }
  .contact-phone { top: 300px; }
  .contact-email { top: 401px; }
  .contact-web { top: 496px; }
</style>
</head>
<body>
<main class="card">
  <section class="brand-panel">
    <div class="brand">
      <span class="brand-mark"></span>
      <span class="brand-name">Harborline Crest</span>
      <span class="brand-tagline">Consulting</span>
    </div>
  </section>
  <div class="divider-line"></div>

  <svg class="contact-rail" viewBox="0 0 72 407" aria-hidden="true">
    <rect x="0" y="0" width="72" height="407" rx="36" fill="var(--green)"/>
    <!-- person -->
    <circle cx="35" cy="37" r="28" fill="var(--navy)"/>
    <circle cx="35" cy="32" r="6" fill="var(--white)"/>
    <path d="M24 46 q11 -13 22 0 v2 h-22z" fill="var(--white)"/>
    <!-- phone -->
    <circle cx="35" cy="166" r="28" fill="var(--navy)"/>
    <path d="M27 156 l4 -2 l4 7 l-3 2 q2 5 7 8 l2 -3 l7 4 l-2 4 q-3 3 -8 0 q-9 -5 -13 -13 q-2 -5 2 -7z" fill="var(--white)"/>
    <!-- envelope -->
    <circle cx="35" cy="270" r="28" fill="var(--navy)"/>
    <rect x="24" y="262" width="22" height="16" rx="1" fill="var(--white)"/>
    <path d="M24 263 l11 9 l11 -9" fill="none" stroke="var(--navy)" stroke-width="1.8"/>
    <!-- globe -->
    <circle cx="35" cy="369" r="28" fill="var(--navy)"/>
    <g fill="none" stroke="var(--white)" stroke-width="1.3">
      <circle cx="35" cy="369" r="11"/>
      <ellipse cx="35" cy="369" rx="5" ry="11"/>
      <line x1="24" y1="369" x2="46" y2="369"/>
      <path d="M26 363 h18 M26 375 h18"/>
    </g>
  </svg>

  <div class="side-tab"></div>

  <h1 class="rep-name"><span class="first">PETER</span> <span class="last">VANCE</span></h1>
  <p class="contact-item contact-phone">833-555-0172</p>
  <p class="contact-item contact-email">pvance@harborlinecrest.com</p>
  <p class="contact-item contact-web">www.harborlinecrest.com</p>
</main>
</body>
</html>
```